Tavin Orsek Website

Website for my son who is in 7th grade in the US. This will prepare him to show people his accomplishments when applying for a job or going to college. It should have:
* A picture (or multiple pictures)
* A resume page
* A place to share your accomplishments
* Links to his other social profiles
* A contact form

Great to include:
* Internships (show some photos of it along with what you’ve learned).
* Volunteer work.
* A side hustle that you want to highlight

Website sample I like:
https://lunafenwick.sitefolio.net/lunafenwickdorra

Target Market(s)

For jobs and colleges admissions.

Number of Pages Required

5+ page

Colors

Requirements
Must have
• * A picture (or multiple pictures)
• * A resume page
• * A place to share your accomplishments
• * Links to his other social profiles
• * A contact form
Nice to have
• Great to include:
• * Internships (show some photos of it along with what you’ve learned).
• * Volunteer work.
• * A side hustle that you want to highlight

```html
<!DOCTYPE html>
<html lang="en">
<head>
<meta charset="utf-8">
<title>Tavin Orsek</title>
<link rel="stylesheet" href="https://fonts.googleapis.com/css2?family=Fira+Sans:ital,wght@1,800&family=Lato:wght@400;700&family=Raleway:wght@600&family=Source+Sans+3:wght@400;600;700&display=swap">
<style>
:root{
  --red:#f0092f;
  --red-deep:#e4202a;
  --ink:#333333;
  --text:#1f1f1f;
  --dark:#1a1a1e;
  --dark-2:#26262c;
  --white:#ffffff;
  --line:#444444;
}
*{box-sizing:border-box;margin:0;padding:0}
html,body{width:1200px;height:2949px;overflow:hidden;background:var(--white)}
body{position:relative;font-family:"Source Sans 3",sans-serif;color:var(--text)}
.abs{position:absolute}

/* header */
.site-header{position:absolute;left:0;top:0;width:1200px;height:102px;background:var(--white)}
.brand{position:absolute;left:218px;top:30px;display:flex;align-items:center;gap:8px;font-family:"Source Sans 3",sans-serif;font-weight:700;font-size:22px;color:var(--red)}
.brand-dot{width:14px;height:14px;border-radius:50%;background:var(--red)}
.contact-chip{position:absolute;top:38px;display:flex;align-items:center;gap:14px;font-family:"Raleway",sans-serif;font-weight:600;font-size:16px;color:#555;letter-spacing:.2px}
.chip-icon{width:38px;height:34px;border:2px solid var(--red);display:flex;align-items:center;justify-content:center}
.main-nav{position:absolute;left:0;top:102px;width:1200px;height:65px;background:var(--red)}
.main-nav a{position:absolute;top:18px;font-family:"Source Sans 3",sans-serif;font-size:23px;color:var(--white);text-decoration:none}

/* hero */
.hero{position:absolute;left:0;top:167px;width:1200px;height:617px;overflow:hidden}
.hero-photo{position:absolute;inset:0;background:linear-gradient(100deg,#9fb3c7 0%,#c8c4c0 30%,#b89a84 55%,#8a6a58 70%,#6f7a8a 100%)}
.hero-title{position:absolute;left:110px;top:215px;font-family:"Fira Sans",sans-serif;font-style:italic;font-weight:800;font-size:72px;line-height:88px;color:var(--white);letter-spacing:-.5px}
.hero-title .accent{color:var(--red-deep)}
.slide-arrow{position:absolute;top:265px;width:52px;height:52px;border-radius:50%;background:var(--red);display:flex;align-items:center;justify-content:center}
.hero-wave{position:absolute;left:0;bottom:0}

/* about */
.about-title{position:absolute;left:111px;top:870px;font-family:"Raleway",sans-serif;font-weight:600;font-size:55px;color:var(--ink)}
.about-text{position:absolute;left:116px;top:956px;width:560px;font-family:"Lato",sans-serif;font-size:15.3px;line-height:24px;color:var(--text)}
.btn{position:absolute;background:var(--red);color:var(--white);display:flex;align-items:center;justify-content:center}
.btn-read{left:111px;top:1137px;width:149px;height:46px;font-size:21px;border-radius:2px}
.about-photo{position:absolute;left:724px;top:885px;width:373px;height:312px;border:6px solid var(--red);background:linear-gradient(135deg,#dfe5e0,#9aa3a0 45%,#4a5a6c 75%,#6a6f68)}

/* highlights */
.highlights-bg{position:absolute;left:0;top:1240px}
.highlight-card{position:absolute;top:1455px;width:314px;height:280px;border:2px solid #e8e8e8}
.card-study{left:111px;background:linear-gradient(135deg,#f1f1f1,#c9c9c9 50%,#5c5652)}
.card-intern{left:447px;background:linear-gradient(135deg,#dce8f0,#a4b6c6 45%,#8a6e5a 70%,#e6e6e6)}
.card-volunteer{left:781px;background:linear-gradient(160deg,#c7d78a,#7e9a3c 45%,#4d6a2a 75%,#5a6fa0)}
.highlight-label{position:absolute;top:1772px;width:314px;text-align:center;font-family:"Source Sans 3",sans-serif;font-weight:600;font-size:30px;color:var(--white)}

/* contact */
.contact-title{position:absolute;left:0;width:1200px;top:1985px;text-align:center;font-family:"Raleway",sans-serif;font-weight:600;font-size:44px;color:var(--ink)}
.field{position:absolute;border:1px solid var(--line);background:var(--white);font-family:"Lato",sans-serif;font-size:11.5px;color:#555;padding:14px 16px}
.field.is-active{border-color:var(--red)}
.btn-send{left:733px;top:2421px;width:193px;height:39px;font-family:"Lato",sans-serif;font-weight:700;font-size:16px;letter-spacing:-.2px}

/* footer */
.footer-wave{position:absolute;left:0;top:2495px}
.site-footer{position:absolute;left:0;top:2574px;width:1200px;height:331px;background:linear-gradient(90deg,var(--dark) 0%,var(--dark-2) 60%,#2a2130 100%)}
.footer-brand{position:absolute;left:150px;top:2760px;width:140px;display:flex;flex-direction:column;align-items:center;gap:12px;font-family:"Source Sans 3",sans-serif;font-weight:700;font-size:25px;color:var(--white)}
.footer-brand .brand-dot{width:20px;height:20px;background:var(--white)}
.footer-info{position:absolute;left:361px;display:flex;align-items:flex-start;gap:14px;font-size:18px;line-height:22px;color:var(--white)}
.footer-info svg{flex:none;margin-top:2px}
.footer-links a{position:absolute;left:638px;font-size:18px;color:var(--white);text-decoration:none}
.subscribe{position:absolute;left:758px;top:2656px;width:334px;height:43px;border-radius:22px;background:var(--white)}
.subscribe .btn{left:237px;top:1px;width:96px;height:41px;border-radius:21px;border:2px solid var(--white);font-size:17px;font-weight:600}
.social{position:absolute;top:2742px;width:18px;height:18px;border-radius:50%;background:var(--white)}
.legal-bar{position:absolute;left:0;top:2905px;width:1200px;height:44px;background:var(--red)}
.legal-bar p{position:absolute;left:116px;top:20px;font-size:13px;color:var(--white)}
</style>
</head>
<body>

<header class="site-header">
  <div class="brand"><span class="brand-dot"></span>Tavin Orsek</div>
  <div class="contact-chip" style="left:677px">
    <span class="chip-icon"><svg width="20" height="14" viewBox="0 0 20 14"><rect x="1" y="1" width="18" height="12" fill="none" stroke="#222" stroke-width="2"/><path d="M1 1 L10 8 L19 1" fill="none" stroke="#222" stroke-width="2"/></svg></span>
    info@tavinorsek.com
  </div>
  <div class="contact-chip" style="left:934px">
    <span class="chip-icon"><svg width="18" height="18" viewBox="0 0 24 24"><path d="M6.6 10.8c1.4 2.8 3.8 5.1 6.6 6.6l2.2-2.2c.3-.3.7-.4 1-.2 1.1.4 2.3.6 3.6.6.6 0 1 .4 1 1V20c0 .6-.4 1-1 1C10.6 21 3 13.4 3 4c0-.6.4-1 1-1h3.5c.6 0 1 .4 1 1 0 1.3.2 2.5.6 3.6.1.3 0 .7-.2 1l-2.3 2.2z" fill="#222"/></svg></span>
    555 014 2290
  </div>
</header>

<nav class="main-nav">
  <a href="#" style="left:315px">Home</a>
  <a href="#" style="left:420px">Portfolio</a>
  <a href="#" style="left:551px">Resume</a>
  <a href="#" style="left:672px">Achievements</a>
  <a href="#" style="left:854px">Blog</a>
  <a href="#" style="left:945px">Contact Us</a>
</nav>

<section class="hero">
  <div class="hero-photo" role="img" aria-label="Portrait of a smiling teenage boy with headphones around his neck in a classroom"></div>
  <h1 class="hero-title">Welcome TO<br><span class="accent">Tavin Orsek</span></h1>
  <span class="slide-arrow" style="left:36px"><svg width="22" height="20" viewBox="0 0 22 20"><path d="M20 10H4M10 3L3 10l7 7" fill="none" stroke="#fff" stroke-width="3.2" stroke-linecap="round" stroke-linejoin="round"/></svg></span>
  <span class="slide-arrow" style="left:1099px"><svg width="22" height="20" viewBox="0 0 22 20"><path d="M2 10h16M12 3l7 7-7 7" fill="none" stroke="#fff" stroke-width="3.2" stroke-linecap="round" stroke-linejoin="round"/></svg></span>
  <svg class="hero-wave" width="1200" height="90" viewBox="0 0 1200 90">
    <path d="M0 33 C300 15 600 25 880 55 C1020 66 1120 52 1200 40 L1200 90 L0 90Z" fill="#e4202a"/>
    <path d="M0 34 C300 16 580 50 820 74 C960 86 1100 76 1200 58 L1200 90 L0 90Z" fill="#ffffff"/>
  </svg>
</section>

<section class="about">
  <h2 class="about-title">About Me</h2>
  <p class="about-text">Lorem ipsum dolor sit amet, consectetur adipiscing elit, sed do eiusmod tempor incid-idunt ut labore et dolore magna aliqua. Quis ipsum suspendisse ultrices gravida. Risus commodo viverra maecenas accumsan lacus vel facilisis. Lorem ipsum dolor sit amet, consectetur adipiscing elit, sed do eiusmod tempor incididunt ut labore et dolore magna aliqua. Quis ipsum suspendisse ultrices gravida. Risus commodo viverra mae-cenas accumsan lacus vel facilisis.</p>
  <a class="btn btn-read">Read More</a>
  <div class="about-photo" role="img" aria-label="Teenage boy sitting on a chair in his bedroom beside a desk"></div>
</section>

<section class="highlights">
  <svg class="highlights-bg" width="1200" height="740" viewBox="0 0 1200 740">
    <defs><linearGradient id="darkFill" x1="0" y1="0" x2="1" y2="1"><stop offset="0" stop-color="#1c1c20"/><stop offset="1" stop-color="#121214"/></linearGradient></defs>
    <path d="M0 115 C250 20 650 15 1200 170 L1200 640 C1000 705 700 735 500 690 C300 660 100 600 0 545 Z" fill="#e4202a"/>
    <path d="M0 145 C250 50 650 40 1200 178 L1200 620 C1000 690 700 720 500 688 C300 660 100 600 0 540 Z" fill="url(#darkFill)"/>
  </svg>
  <div class="highlight-card card-study" role="img" aria-label="Student writing notes at a desk"></div>
  <div class="highlight-card card-intern" role="img" aria-label="Boy working on a laptop during an internship"></div>
  <div class="highlight-card card-volunteer" role="img" aria-label="Volunteers planting a tree in a park"></div>
  <h3 class="highlight-label" style="left:111px">Accomplishments</h3>
  <h3 class="highlight-label" style="left:447px">Internships</h3>
  <h3 class="highlight-label" style="left:781px;top:1775px">Volunteer work</h3>
</section>

<section class="contact">
  <h2 class="contact-title">Contact Us</h2>
  <div class="field is-active" style="left:270px;top:2092px;width:317px;height:42px">Your Name...</div>
  <div class="field" style="left:613px;top:2092px;width:317px;height:42px">Last Name...</div>
  <div class="field" style="left:270px;top:2155px;width:317px;height:42px">Phone No...</div>
  <div class="field" style="left:613px;top:2155px;width:317px;height:42px">Email Address...</div>
  <div class="field" style="left:270px;top:2226px;width:660px;height:149px">Your Messages.....</div>
  <a class="btn btn-send">SEND MESSAGES</a>
</section>

<svg class="footer-wave" width="1200" height="80" viewBox="0 0 1200 80">
  <path d="M0 47 C150 15 300 8 500 22 L1200 55 L1200 80 L0 80Z" fill="#e4202a"/>
  <path d="M0 60 C200 30 400 24 600 34 C800 44 1000 56 1200 50 L1200 80 L0 80Z" fill="#1a1a1e"/>
</svg>
<footer class="site-footer"></footer>

<div class="footer-brand"><span class="brand-dot"></span>Tavin Orsek</div>

<div class="footer-info" style="top:2660px">
  <svg width="18" height="22" viewBox="0 0 18 22"><path d="M9 1C4.6 1 1.5 4.3 1.5 8.5 1.5 14 9 21 9 21s7.5-7 7.5-12.5C16.5 4.3 13.4 1 9 1z" fill="#fff"/><circle cx="9" cy="8.5" r="3" fill="#1a1a1e"/></svg>
  <span>742 Harbor Crest Lane<br>Marlow Bay, CA 90417</span>
</div>
<div class="footer-info" style="top:2731px">
  <svg width="18" height="18" viewBox="0 0 24 24"><path d="M6.6 10.8c1.4 2.8 3.8 5.1 6.6 6.6l2.2-2.2c.3-.3.7-.4 1-.2 1.1.4 2.3.6 3.6.6.6 0 1 .4 1 1V20c0 .6-.4 1-1 1C10.6 21 3 13.4 3 4c0-.6.4-1 1-1h3.5c.6 0 1 .4 1 1 0 1.3.2 2.5.6 3.6.1.3 0 .7-.2 1l-2.3 2.2z" fill="#fff"/></svg>
  <span>Tel: (555) 013-7781</span>
</div>
<div class="footer-info" style="top:2779px">
  <svg width="20" height="14" viewBox="0 0 20 14"><rect x="1" y="1" width="18" height="12" fill="none" stroke="#fff" stroke-width="1.6"/><path d="M1 1 L10 8 L19 1" fill="none" stroke="#fff" stroke-width="1.6"/></svg>
  <span>mara@brightlanestudio.com</span>
</div>

<nav class="footer-links">
  <a href="#" style="top:2653px">Home</a>
  <a href="#" style="top:2687px">About</a>
  <a href="#" style="top:2722px;left:642px">Product</a>
  <a href="#" style="top:2756px;left:642px">Vape Life</a>
  <a href="#" style="top:2790px;left:642px">Store</a>
  <a href="#" style="top:2825px">Contact Us</a>
</nav>

<div class="subscribe"><a class="btn">Send</a></div>

<span class="social" style="left:775px" aria-label="Social profile"></span>
<span class="social" style="left:824px" aria-label="Social profile"></span>
<span class="social" style="left:877px" aria-label="Social profile"></span>
<span class="social" style="left:929px" aria-label="Social profile"></span>
<span class="social" style="left:974px" aria-label="Social profile"></span>

<div class="legal-bar"><p>© 2019 All Rights Reserved | Privacy Policy | Terms and Conditions</p></div>

</body>
</html>
```